Heronfield Wealth Advisors, Inc. Marketing Collateral - 401k Rollover Decisions

We are looking to create a branded one-pager marketing collateral piece talking about 401k Rollovers & the important information people should know. Rough draft of concept & content included below, and we will finalize copy later. Would include a call to action to contact us. Our website and other contact information are available at https://growwithheronfield.com/.

Target Market(s)

Working adults ages 55-75 with access to retirement accounts or who have a 401k account. Especially interested in appealing to people who work for small businesses, local businesses, have company stock, and other unique needs in this space.

Industry/Entity Type

Financial services

Font styles to use
Other font styles liked:
• Cambria

Requirements
Must have
• Clear message & call to action
Nice to have
• Highlight how many Americans have been changing jobs since COVID and why it would be worth working with a professional to make decisions on what to do with retirement accounts and assets. (We're working on getting that stat)
Should not have
• Too much text, don't want to inundate with text blocks

```html
<!DOCTYPE html>
<html lang="en">
<head>
<meta charset="utf-8">
<title>Heronfield Wealth Advisors – 401(k) Rollover Decisions</title>
<link href="https://fonts.googleapis.com/css2?family=Merriweather:wght@400&family=Roboto:wght@400;700&display=swap" rel="stylesheet">
<style>
:root{
  --red:#c4222d;
  --red-dark:#8e1a22;
  --ink:#1c1c1c;
  --paper:#ffffff;
  --rule:#e3e3e3;
  --table-head:#f1f1f1;
  --backdrop:#d9d9d9;
}
*{margin:0;padding:0;box-sizing:border-box}
html,body{width:990px;height:1200px;overflow:hidden;background:var(--backdrop)}
.flyer{position:absolute;left:31px;top:0;width:927px;height:1200px;background:var(--paper);overflow:hidden;font-family:"Roboto",Arial,sans-serif;color:var(--ink)}
.hero-photo{position:absolute;left:0;top:0;width:927px;height:437px;
  background:radial-gradient(ellipse at 72% 35%,#d8cbbd 0%,#b3a495 35%,transparent 65%),
             linear-gradient(100deg,#6f645b 0%,#8e8378 40%,#a2968a 70%,#c9c0b6 100%)}
.brand{position:absolute;left:54px;top:250px;width:344px;text-align:center;color:#fff;font-family:"Merriweather",Georgia,serif;font-weight:400}
.brand-name{font-size:40px;letter-spacing:1px;line-height:1}
.brand-sub{font-size:14px;letter-spacing:2.5px;margin-top:8px;text-transform:uppercase}
.option{position:absolute;left:54px;width:344px;background:#fff;border:1px solid var(--rule);box-shadow:0 1px 3px rgba(0,0,0,.08)}
.option-title{background:var(--red);color:#fff;font-family:"Merriweather",Georgia,serif;font-size:24px;height:41px;line-height:40px;padding-left:42px}
.option-text{font-size:13.4px;line-height:18px;padding:12px 14px 0 42px}
.cta-tab{position:absolute;left:54px;top:1043px;width:200px;height:39px;background:var(--red);color:#fff;font-weight:700;font-size:26px;line-height:39px;padding-left:29px;clip-path:polygon(0 0,175px 0,200px 100%,0 100%)}
.cta-rule{position:absolute;left:54px;top:1081px;width:344px;height:1.5px;background:var(--red)}
.cta-phone{position:absolute;left:82px;top:1098px;display:flex;align-items:center;gap:6px;font-weight:700;font-size:34px;letter-spacing:.5px}
.cta-web{position:absolute;left:85px;top:1143px;font-size:17.5px;letter-spacing:1px}
.cta-web b{color:var(--red);font-weight:400}
.quote{position:absolute;left:432px;top:337px;width:440px;height:250px;background:var(--red);color:#fff}
.quote-bar{position:absolute;left:44px;top:30px;width:2px;height:192px;background:#fff}
.quote-text{position:absolute;left:65px;top:26px;width:350px;font-family:"Merriweather",Georgia,serif;font-size:25px;line-height:32.5px}
.quote-fold{position:absolute;right:0;bottom:0}
.body-copy{position:absolute;left:432px;top:613px;width:440px;font-size:14.6px;line-height:18.2px;text-align:justify}
.body-copy p+p{margin-top:15px}
.compare{position:absolute;left:432px;top:879px;width:441px;border:1px solid var(--rule);border-collapse:collapse;background:#fff}
.compare caption{background:var(--red);color:#fff;font-family:"Merriweather",Georgia,serif;font-size:24px;height:48px;line-height:47px;text-align:center}
.compare th{background:var(--table-head);text-align:left;font-size:25px;font-weight:700;height:41px;padding-left:31px}
.compare td{vertical-align:top;font-size:13.8px;line-height:17.5px;padding:9px 10px 0 31px;position:relative;border-top:1px solid var(--rule)}
.compare td+td,.compare th+th{border-left:1px solid var(--rule)}
.compare td svg{position:absolute;left:15px;top:12px}
.row-1 td{height:50px}.row-2 td{height:70px}.row-3 td{height:71px}
.footer-band{position:absolute;left:0;bottom:0;width:927px;height:7px;background:linear-gradient(90deg,var(--red),var(--red) 70%,var(--red-dark))}
</style>
</head>
<body>
<main class="flyer">
  <div class="hero-photo" role="img" aria-label="Photo of a smiling retired couple sharing a blanket on a rocky beach with driftwood"></div>

  <div class="brand">
    <div class="brand-name">HERONFIELD</div>
    <div class="brand-sub">Wealth Advisors, Inc.</div>
  </div>

  <section class="option" style="top:416px;height:106px">
    <h2 class="option-title">Leave it</h2>
    <p class="option-text">Most employer plans allow you to leave the funds within the qualified plan</p>
  </section>
  <section class="option" style="top:548px;height:125px">
    <h2 class="option-title">Roll it</h2>
    <p class="option-text">Depending on the type of qualified plan, you can roll the funds over from the employer plan to an IRA.</p>
  </section>
  <section class="option" style="top:700px;height:146px">
    <h2 class="option-title">Move it</h2>
    <p class="option-text">If you've started working at a new company, they will often have their own qualified plan available that you can move your old company's funds to.</p>
  </section>
  <section class="option" style="top:873px;height:141px">
    <h2 class="option-title">Take it</h2>
    <p class="option-text">There is the option to take the account in cash, but it is not typically advisable due to the tax and potential penalty implications.</p>
  </section>

  <div class="cta-tab">talk to us</div>
  <div class="cta-rule"></div>
  <div class="cta-phone">
    <svg width="28" height="28" viewBox="0 0 28 28" aria-hidden="true"><circle cx="14" cy="14" r="12.5" fill="none" stroke="#c4222d" stroke-width="2"/><path d="M9.5 8.5c.8-.8 1.6-.6 2 .1l1.2 2c.3.6.1 1.1-.4 1.5l-.7.5c.7 1.6 1.9 2.9 3.6 3.7l.5-.7c.4-.5 1-.7 1.5-.4l2 1.2c.7.4.8 1.3.1 2-1.3 1.3-3 1.5-5.3.1-2.5-1.5-4.3-3.5-5.2-5.8-.6-1.6-.4-2.8.7-3.2z" fill="#c4222d"/></svg>
    555-014-2270
  </div>
  <div class="cta-web">www.<b>GrowWithHeronfield</b>.com</div>

  <aside class="quote">
    <div class="quote-bar"></div>
    <p class="quote-text">The most important thing to realize when leaving an employer is that you have options for the money that you have worked hard for and saved.</p>
    <svg class="quote-fold" width="27" height="27" viewBox="0 0 27 27" aria-hidden="true"><polygon points="27,0 27,27 0,27" fill="#fff"/></svg>
  </aside>

  <div class="body-copy">
    <p>It is important to work with a fiduciary to help you evaluate your options and the pros and cons of them. A fiduciary is someone who is obligated to provide you unbiased advice and disclose any conflicts of interest in their recommendations. It can be particularly important to work with a fiduciary if you are retiring early or are generally confused about all of the information and misinformation out there.</p>
    <p>We recommend working with an expert who has experience with a multitude of different types of qualified plans such as 401(k), 403(b), Employee Stock Ownership Plans, SEP IRAs, etc. Not all plan types are eligible for rollovers, and even if they are, they may vary in the types of plans that they can be rolled in to.</p>
  </div>

  <table class="compare">
    <caption>Rolling over 401(k) assets to IRA</caption>
    <tr><th style="width:243px">PROS</th><th>CONS</th></tr>
    <tr class="row-1">
      <td><svg width="11" height="11" viewBox="0 0 11 11"><circle cx="5.5" cy="5.5" r="4.8" fill="none" stroke="#c4222d"/><path d="M3.2 5.6l1.6 1.5 3-3" fill="none" stroke="#c4222d"/></svg>Typically more investment choices in an IRA</td>
      <td><svg width="11" height="11" viewBox="0 0 11 11"><circle cx="5.5" cy="5.5" r="4.8" fill="none" stroke="#c4222d"/><path d="M3.2 5.6l1.6 1.5 3-3" fill="none" stroke="#c4222d"/></svg>Less protection from creditors</td>
    </tr>
    <tr class="row-2">
      <td><svg width="11" height="11" viewBox="0 0 11 11"><circle cx="5.5" cy="5.5" r="4.8" fill="none" stroke="#c4222d"/><path d="M3.2 5.6l1.6 1.5 3-3" fill="none" stroke="#c4222d"/></svg>Ability to make contributions to the account even after leaving your former employer</td>
      <td><svg width="11" height="11" viewBox="0 0 11 11"><circle cx="5.5" cy="5.5" r="4.8" fill="none" stroke="#c4222d"/><path d="M3.2 5.6l1.6 1.5 3-3" fill="none" stroke="#c4222d"/></svg>Less access to funds prior to age 59½</td>
    </tr>
    <tr class="row-3">
      <td><svg width="11" height="11" viewBox="0 0 11 11"><circle cx="5.5" cy="5.5" r="4.8" fill="none" stroke="#c4222d"/><path d="M3.2 5.6l1.6 1.5 3-3" fill="none" stroke="#c4222d"/></svg>Choice of investment custodian and investment advisor you work with</td>
      <td><svg width="11" height="11" viewBox="0 0 11 11"><circle cx="5.5" cy="5.5" r="4.8" fill="none" stroke="#c4222d"/><path d="M3.2 5.6l1.6 1.5 3-3" fill="none" stroke="#c4222d"/></svg>RMDs on funds at age 72 regardless if you are still working</td>
    </tr>
  </table>

  <div class="footer-band"></div>
</main>
</body>
</html>
```